Hollow Meridian - a Thriller Novel

A thriller set in Antarctica. I'm envisioning an image of the entire continent as viewed from above, white and icy and surrounded by stormy seas if you can tell that much, but the entire continent filled with a colorful cymatic image (if you Google image these you'll see what I mean -- any pattern will do if it looks right, and if it's royalty-free). An alternative: icy white scene viewed from the front like normal, with the colorful cymatic image on top.
Title is "Hollow Meridian". Author is R.J. Penwick
Here's one cymatic image: https://www.plinkseek-example.net/img/view?ref=tovalgallery-example.org%2Fpatterns%2Fwave-study-inset3.jpg
Here's a bunch more: https://www.plinkseek-example.net/img/view?ref=brelomi-example.org%2Fpatterns%2Fwave-grid.jpg
But of course, something royalty-free or similar. I believe they are all circular fractal patterns, for whatever that's worth.
new adult, adult

```html
<!DOCTYPE html>
<html lang="en">
<head>
<meta charset="utf-8">
<title>Hollow Meridian — R.J. Penwick</title>
<link href="https://fonts.googleapis.com/css2?family=Bebas+Neue&family=Oswald:wght@200;300&display=swap" rel="stylesheet">
<style>
  :root {
    --page: #e9e9ea;
    --navy-deep: #1f2c44;
    --navy: #2a3b58;
    --navy-soft: #34496a;
    --ice-white: #dde7ec;
    --ice-pale: #b9cdd7;
    --ice-mid: #7f9fb1;
    --ice-teal: #4f7d8d;
    --sea-deep: #2c4560;
    --ink-white: #ffffff;
  }
  html, body {
    margin: 0;
    width: 1200px;
    height: 1000px;
    overflow: hidden;
    background: var(--page);
  }
  .book-cover {
    position: absolute;
    left: 300px;
    top: 50px;
    width: 600px;
    height: 900px;
    overflow: hidden;
    background: linear-gradient(180deg, var(--navy-deep) 0%, var(--navy) 50%, var(--navy-soft) 100%);
  }
  .ice-scene {
    position: absolute;
    left: 0;
    right: 0;
    top: 470px;
    bottom: 0;
    background:
      linear-gradient(180deg,
        rgba(42,59,88,0) 0%,
        rgba(127,159,177,0.35) 30%,
        rgba(185,205,215,0.45) 44%,
        rgba(79,125,141,0.40) 47%,
        rgba(44,69,96,0.55) 70%,
        rgba(31,44,68,0.70) 100%);
  }
  .horizon-line {
    position: absolute;
    left: 0;
    right: 0;
    top: 676px;
    height: 2px;
    background: rgba(221,231,236,0.35);
  }
  .crystal-medallion {
    position: absolute;
    left: 34px;
    top: 400px;
    width: 532px;
    height: 532px;
  }
  .author-name {
    position: absolute;
    top: 46px;
    right: 64px;
    margin: 0;
    font-family: "Oswald", sans-serif;
    font-weight: 300;
    font-size: 21px;
    letter-spacing: 0.32em;
    color: var(--ink-white);
  }
  .title {
    margin: 0;
    font-weight: normal;
    color: var(--ink-white);
  }
  .title-inverted {
    position: absolute;
    top: 96px;
    right: 44px;
    font-family: "Bebas Neue", sans-serif;
    font-size: 190px;
    line-height: 0.8;
    letter-spacing: 0.01em;
    transform: rotate(180deg);
  }
  .title-upright {
    position: absolute;
    top: 258px;
    right: 50px;
    font-family: "Oswald", sans-serif;
    font-weight: 200;
    font-size: 124px;
    line-height: 1;
  }
</style>
</head>
<body>
  <main class="book-cover">
    <div class="ice-scene" role="img" aria-label="Icy Antarctic landscape with snowy mountains reflected in still polar water"></div>
    <div class="horizon-line"></div>

    <svg class="crystal-medallion" viewBox="0 0 532 532" role="img" aria-label="Circular cymatic ice-crystal pattern of shard-like petals radiating from a star-shaped centre, mirrored across the horizon">
      <defs>
        <clipPath id="medallion-clip">
          <circle cx="266" cy="266" r="264"/>
        </clipPath>
        <linearGradient id="upper-ice" x1="0" y1="0" x2="0" y2="1">
          <stop offset="0%" stop-color="#7f9fb1" stop-opacity="0.35"/>
          <stop offset="60%" stop-color="#b9cdd7" stop-opacity="0.7"/>
          <stop offset="100%" stop-color="#dde7ec" stop-opacity="0.85"/>
        </linearGradient>
        <linearGradient id="lower-sea" x1="0" y1="0" x2="0" y2="1">
          <stop offset="0%" stop-color="#b9cdd7" stop-opacity="0.75"/>
          <stop offset="35%" stop-color="#7f9fb1" stop-opacity="0.6"/>
          <stop offset="100%" stop-color="#4f7d8d" stop-opacity="0.35"/>
        </linearGradient>
        <radialGradient id="core-glow" cx="50%" cy="50%" r="50%">
          <stop offset="0%" stop-color="#ffffff" stop-opacity="0.75"/>
          <stop offset="30%" stop-color="#dde7ec" stop-opacity="0.45"/>
          <stop offset="70%" stop-color="#7f9fb1" stop-opacity="0.1"/>
          <stop offset="100%" stop-color="#4f7d8d" stop-opacity="0"/>
        </radialGradient>
        <radialGradient id="rim-shade" cx="50%" cy="50%" r="50%">
          <stop offset="70%" stop-color="#1f2c44" stop-opacity="0"/>
          <stop offset="100%" stop-color="#1f2c44" stop-opacity="0.45"/>
        </radialGradient>
      </defs>
      <g clip-path="url(#medallion-clip)">
        <rect x="0" y="0" width="532" height="266" fill="url(#upper-ice)"/>
        <rect x="0" y="266" width="532" height="266" fill="url(#lower-sea)"/>
        <circle cx="266" cy="266" r="264" fill="url(#core-glow)"/>
        <circle cx="266" cy="266" r="264" fill="url(#rim-shade)"/>
      </g>
      <circle cx="266" cy="266" r="264" fill="none" stroke="#b9cdd7" stroke-opacity="0.4" stroke-width="1.5"/>
    </svg>

    <p class="author-name">R.J. PENWICK</p>
    <h1 class="title">
      <span class="title-inverted">HOLLOW</span>
      <span class="title-upright">MERIDIAN</span>
    </h1>
  </main>
</body>
</html>
```